The Hidden Storm Beneath Your Garden Book Cover

Need a book cover that jumps out, simple is good. I am trying to relay to readers that they face a serious tax burden when they reach retirement.

I am attaching the cover I've been using, which I designed, but it's not nearly effective enough.
Get rid of the word "Accounts" in the cover, please.

```html
<!DOCTYPE html>
<html lang="en">
<head>
<meta charset="utf-8">
<title>The Hidden Storm Beneath Your Garden – Book Cover</title>
<link rel="stylesheet" href="https://fonts.googleapis.com/css2?family=Josefin+Sans:wght@300;400;600;700&family=Nunito:wght@600;700&family=Open+Sans:wght@300;400;600;700&family=Cormorant+Garamond:wght@500&display=swap">
<style>
  :root {
    --navy: #08344a;
    --gold: #c29455;
    --sand: #ecdfcd;
    --panel: #e6e6e6;
    --grey-text: #8b8d8f;
    --body-text: #4a4a4a;
    --olive: #6e6850;
    --paper: #ffffff;
    --teal: #4aa6b8;
  }
  * { margin: 0; padding: 0; box-sizing: border-box; }
  html, body { width: 1200px; height: 960px; overflow: hidden; background: var(--paper); }
  .stage { position: relative; width: 1200px; height: 960px; }

  /* Back cover */
  .back-cover {
    position: absolute; left: 54px; top: 56px; width: 531px; height: 841px;
    background: var(--gold); box-shadow: 0 2px 6px rgba(0,0,0,.25);
  }
  .back-panel {
    position: absolute; left: 28px; top: 27px; width: 476px; height: 787px;
    background: var(--panel);
  }
  .benefit {
    position: absolute; display: flex; align-items: center; gap: 10px;
    font-family: "Nunito", sans-serif; font-weight: 600; font-size: 11.5px;
    line-height: 1.2; color: var(--navy);
  }
  .benefit svg { width: 32px; height: 32px; flex: none; }
  .benefit b { font-weight: 700; }
  .benefit.b1 { left: 50px; top: 58px; }
  .benefit.b2 { left: 238px; top: 57px; }
  .benefit.b3 { left: 50px; top: 112px; }
  .benefit.b4 { left: 238px; top: 111px; }

  .author-photo {
    position: absolute; left: 136px; top: 199px; width: 173px; height: 194px;
    background: linear-gradient(160deg, #4d5a4a 0%, #8b7d6e 40%, #7c7f80 70%, #a9a19a 100%);
  }
  .author-credit {
    position: absolute; left: 0; right: 0; top: 408px; text-align: center;
    font-family: "Open Sans", sans-serif; font-size: 12.5px; line-height: 15.5px;
    color: #1b1b1b; font-weight: 600;
  }
  .author-credit .author-name {
    font-family: "Josefin Sans", sans-serif; font-weight: 600; font-size: 21px;
    letter-spacing: .5px; color: #1b1b1b; line-height: 22px; margin-bottom: 1px;
  }
  .author-credit .accent { color: var(--gold); }
  .author-bio {
    position: absolute; left: 130px; width: 216px; text-align: center;
    font-family: "Open Sans", sans-serif; font-weight: 300; font-size: 11.6px;
    line-height: 15.2px; color: var(--body-text);
  }
  .author-bio strong { font-weight: 600; color: #222; }
  .author-bio.first { top: 517px; left: 112px; width: 252px; }
  .author-bio.second { top: 647px; left: 112px; width: 252px; }
  .back-rule { position: absolute; left: 126px; top: 757px; width: 226px; height: 6px; }

  /* Front cover */
  .front-cover {
    position: absolute; left: 609px; top: 54px; width: 528px; height: 841px;
    background: var(--paper); overflow: hidden; box-shadow: 0 2px 6px rgba(0,0,0,.25);
  }
  .corner-motif {
    position: absolute; left: 19px; top: 0; width: 176px; height: 190px;
    background: linear-gradient(180deg, var(--sand), rgba(236,223,205,.7));
    border-radius: 0 60px 90px 0;
  }
  .publisher-mark {
    position: absolute; left: 316px; top: 48px; display: flex; align-items: center; gap: 8px;
    font-family: "Josefin Sans", sans-serif; font-weight: 400; font-size: 17px;
    letter-spacing: 1px; color: var(--teal); line-height: 1;
  }
  .publisher-mark .dot { width: 22px; height: 22px; border-radius: 50%; background: var(--teal); }
  .title {
    position: absolute; left: 45px; top: 218px; z-index: 2;
    font-family: "Josefin Sans", sans-serif; font-weight: 700; font-size: 56px;
    line-height: 65px; color: var(--navy); letter-spacing: .5px;
  }
  .title span { display: block; height: 65px; }
  .title .hot { color: var(--gold); }
  .cover-portrait { position: absolute; left: 266px; top: 222px; width: 258px; height: 262px; }
  .subtitle {
    position: absolute; left: 49px; top: 549px;
    font-family: "Josefin Sans", sans-serif; font-weight: 700; font-size: 25px;
    line-height: 32px; letter-spacing: 1.3px; color: var(--grey-text);
  }
  .subtitle-bang {
    position: absolute; left: 422px; top: 538px;
    font-family: "Josefin Sans", sans-serif; font-weight: 700; font-size: 66px;
    line-height: 66px; color: var(--grey-text);
  }
  .author-band {
    position: absolute; left: 0; right: 0; bottom: 0; height: 181px; background: var(--navy);
  }
  .band-name {
    position: absolute; left: 0; right: 0; top: 38px; text-align: center;
    font-family: "Josefin Sans", sans-serif; font-weight: 400; font-size: 56px;
    letter-spacing: .5px; color: var(--olive); line-height: 1;
  }
  .band-url {
    position: absolute; left: 0; right: 0; top: 106px; text-align: center;
    font-family: "Cormorant Garamond", serif; font-weight: 500; font-size: 13px;
    letter-spacing: 7px; color: #c9c9c9;
  }
</style>
</head>
<body>
<main class="stage">

  <section class="back-cover" aria-label="Back cover">
    <div class="back-panel">
      <div class="benefit b1">
        <svg viewBox="0 0 32 32"><circle cx="16" cy="16" r="14.5" fill="none" stroke="var(--navy)" stroke-width="2"/><rect x="9" y="14" width="14" height="8" fill="none" stroke="var(--navy)" stroke-width="1.6"/><path d="M11 11l10 3" stroke="var(--navy)" stroke-width="1.6"/></svg>
        <span><b>REDUCE</b> income tax</span>
      </div>
      <div class="benefit b2">
        <svg viewBox="0 0 32 32"><circle cx="16" cy="16" r="14.5" fill="none" stroke="var(--navy)" stroke-width="2"/><path d="M8 16l8-7 8 7" fill="none" stroke="var(--navy)" stroke-width="1.8"/><rect x="11" y="15" width="10" height="8" fill="var(--navy)"/></svg>
        <span><b>ELIMINATE</b> social security tax</span>
      </div>
      <div class="benefit b3">
        <svg viewBox="0 0 32 32"><circle cx="16" cy="16" r="14.5" fill="none" stroke="var(--navy)" stroke-width="2"/><path d="M13 8h6v5h5v6h-5v5h-6v-5H8v-6h5z" fill="var(--navy)"/></svg>
        <span><b>AVOID</b> huge Medicare<br>premium increases</span>
      </div>
      <div class="benefit b4">
        <svg viewBox="0 0 32 32"><circle cx="16" cy="16" r="14.5" fill="none" stroke="var(--navy)" stroke-width="2"/><rect x="9" y="9" width="14" height="14" fill="none" stroke="var(--navy)" stroke-width="1.5"/><path d="M12 21v-4M15 21v-6M18 21v-3M21 21v-8M11 16l4-4 3 2 4-4" stroke="var(--navy)" stroke-width="1.5" fill="none"/></svg>
        <span><b>LEAVE</b> a tax-free legacy</span>
      </div>

      <div class="author-photo" role="img" aria-label="Portrait photo of the author in a grey suit, outdoors"></div>

      <div class="author-credit">
        <div class="author-name">DALE&nbsp; MARROW</div>
        is a <span class="accent">CERTIFIED FINANCIAL PLANNER</span><br>
        andholds<br>
        <span class="accent">a Master’s degree</span><br>
        <span class="accent">in Personal Financial Planning</span>
      </div>

      <p class="author-bio first">Dale has provided financial advice to clients since 1998. Over those 2 decades he has developed extensive knowledge of <strong>Investment Management, Social Security, Tax, Retirement Planning</strong> and wealth transfer strategies.</p>
      <p class="author-bio second">He has learned that successful financial planning does not need to be complex. He follows the tried and true tule he learned in the Army, “Keep It Simple.”</p>

      <svg class="back-rule" viewBox="0 0 226 6"><line x1="3" y1="3" x2="223" y2="3" stroke="var(--gold)" stroke-width="1"/><circle cx="3" cy="3" r="2.5" fill="var(--gold)"/><circle cx="223" cy="3" r="2.5" fill="var(--gold)"/></svg>
    </div>
  </section>

  <section class="front-cover" aria-label="Front cover">
    <div class="corner-motif" role="img" aria-label="Large soft beige dollar-sign motif in the corner"></div>

    <div class="publisher-mark"><span class="dot"></span>LINDEN WEALTH PLANNING</div>

    <h1 class="title">
      <span>THE</span>
      <span class="hot">HIDDEN</span>
      <span class="hot">STORM</span>
      <span>BENEATH</span>
      <span>YOUR GARDEN</span>
    </h1>

    <svg class="cover-portrait" viewBox="0 0 258 262">
      <circle cx="125" cy="118" r="114" fill="#dfe6ee" role="img" aria-label="Photo of a worried older man holding his forehead"/>
      <path d="M210 22 A128 128 0 0 1 95 245 A122 122 0 0 0 210 22 Z" fill="var(--gold)"/>
    </svg>

    <p class="subtitle">AND HOW THE ROTH IRA<br>CAN HELP YOU AVOID IT</p>
    <span class="subtitle-bang">!</span>

    <div class="author-band">
      <div class="band-name">DALE MARROW</div>
      <div class="band-url">WWW.lindenwealthplanning.com</div>
    </div>
  </section>

</main>
</body>
</html>
```